Email Signiture and letterhead design

we are looking for a modern business design to incorporate our logo and qel certification plus social icons for Vorlant, Pelmora, and zandoro
they must include our UK vat and also company registration as text but I can fill these out. Email signature to have a link/icon to our webshop www.trexolan.co.uk

Target Market(s)

All

Font styles to use
Serif
Sans Serif

Requirements
Must have
• Address, tel, email , web details incorperated
Nice to have
• a professional looking letter head and email signiture, Email signature to have a link/icon to our webshop www.trexolan.co.uk

```html
<!DOCTYPE html>
<html lang="en">
<head>
<meta charset="utf-8">
<title>Daventa Hubs &amp; Axles Ltd – Letterhead and Email Signature</title>
<link href="https://fonts.googleapis.com/css2?family=Montserrat:wght@400;500;600;700&family=Questrial&display=swap" rel="stylesheet">
<style>
  :root {
    --red: #ed1c24;
    --ink: #2b2b2b;
    --body: #7b7b7b;
    --faint: #f1f1f2;
    --backdrop: #e4e5e7;
    --paper: #ffffff;
  }
  * { box-sizing: border-box; margin: 0; padding: 0; }
  html, body { width: 1200px; height: 898px; overflow: hidden; }
  body { background: var(--backdrop); position: relative; font-family: "Montserrat", sans-serif; color: var(--ink); }

  .sheet { position: absolute; background: var(--paper); box-shadow: 2px 3px 8px rgba(0,0,0,.18); overflow: hidden; }

  /* Letterhead */
  .letterhead { left: 50px; top: 69px; width: 541px; height: 760px; }
  .brand { position: absolute; display: flex; align-items: center; gap: 5px; color: var(--ink); font-family: "Montserrat", sans-serif; font-weight: 700; white-space: nowrap; line-height: 1; }
  .brand-dot { width: 10px; height: 10px; border-radius: 50%; background: var(--red); flex: none; }
  .letterhead .brand { left: 22px; top: 66px; font-size: 10.5px; }
  .header-rule { position: absolute; left: 190px; top: 73px; width: 218px; height: 1px; background: var(--red); }
  .contact-list { position: absolute; left: 412px; top: 36px; list-style: none; font-size: 11px; line-height: 14px; color: var(--ink); }
  .contact-list li { display: flex; align-items: center; gap: 4px; }
  .icon { width: 9px; height: 9px; flex: none; }

  .recipient { position: absolute; left: 25px; top: 187px; font-size: 10.5px; line-height: 17px; color: var(--ink); }
  .recipient-name { font-size: 20px; font-weight: 600; color: var(--red); line-height: 22px; letter-spacing: .2px; }
  .recipient .addr { line-height: 13px; margin-top: 2px; }
  .letter-date { position: absolute; right: 25px; top: 257px; font-size: 11.5px; font-weight: 600; color: var(--ink); }

  .letter-body { position: absolute; left: 22px; width: 495px; font-family: "Questrial", sans-serif; font-size: 10.8px; line-height: 12.5px; color: var(--body); text-align: justify; }
  .p1 { top: 295px; }
  .p2 { top: 382px; }
  .p3 { top: 470px; }

  .signoff { position: absolute; left: 40px; top: 546px; font-family: "Questrial", sans-serif; font-size: 13px; color: var(--ink); }
  .signature { position: absolute; left: 49px; top: 573px; width: 86px; height: 53px; background: linear-gradient(90deg, #f6f6f6, #ececec); border-radius: 3px; }

  .decor { position: absolute; background: radial-gradient(ellipse at 55% 100%, var(--faint) 0%, rgba(241,241,242,.6) 45%, rgba(255,255,255,0) 72%); }
  .letterhead .decor { left: 10px; top: 640px; width: 420px; height: 120px; }

  .address-band { position: absolute; left: 392px; top: 684px; width: 149px; height: 55px; background: var(--red); color: #fff; font-size: 9.5px; line-height: 10.7px; padding: 12px 0 0 24px; }
  .address-band .pin { position: absolute; left: 11px; top: 12px; width: 9px; height: 12px; }

  /* Email signature */
  .signature-card { left: 610px; top: 381px; width: 540px; height: 137px; }
  .signature-card .brand { left: 15px; top: 53px; font-size: 8.5px; gap: 4px; }
  .signature-card .brand-dot { width: 8px; height: 8px; }
  .signature-card .decor { left: 0; top: 55px; width: 260px; height: 82px; }
  .sender-name { position: absolute; left: 263px; top: 43px; font-size: 19px; font-weight: 700; color: var(--ink); line-height: 24px; }
  .sender-role { position: absolute; left: 263px; top: 65px; font-size: 9.5px; color: var(--ink); line-height: 12px; }
  .role-rule { position: absolute; left: 307px; top: 72px; width: 233px; height: 1px; background: #555; }
  .info-band { position: absolute; left: 243px; top: 80px; width: 297px; height: 45px; background: var(--red); clip-path: polygon(2% 0, 100% 0, 100% 100%, 0 100%); color: #fff; font-size: 6.6px; line-height: 9px; }
  .info-band .contacts { position: absolute; left: 20px; top: 8.5px; list-style: none; }
  .info-band .contacts li { display: flex; align-items: center; gap: 2px; }
  .info-band .contacts .icon { width: 6px; height: 6px; }
  .info-band .postal { position: absolute; left: 98px; top: 8.5px; }
  .follow { position: absolute; left: 163px; top: 9px; width: 110px; text-align: center; }
  .follow-title { font-weight: 600; font-size: 6.2px; }
  .social { display: flex; justify-content: center; gap: 5px; margin-top: 4px; }
  .social span { display: flex; align-items: center; gap: 2px; font-size: 5.6px; }
  .social i { width: 8px; height: 8px; border: 1px solid #fff; border-radius: 50%; display: block; }
</style>
</head>
<body>

<section class="sheet letterhead">
  <div class="brand"><span class="brand-dot"></span>Daventa Hubs &amp; Axles Ltd</div>
  <div class="header-rule"></div>
  <ul class="contact-list">
    <li><svg class="icon" viewBox="0 0 10 10"><circle cx="5" cy="5" r="5" fill="#ed1c24"/><path d="M3.2 2.6l1 .9-.5.8a3.5 3.5 0 0 0 2 2l.8-.5.9 1-.7.8A5 5 0 0 1 2.4 3.3z" fill="#fff"/></svg>161 480 2291</li>
    <li><svg class="icon" viewBox="0 0 10 10"><circle cx="5" cy="5" r="5" fill="#ed1c24"/><rect x="2.6" y="3.3" width="4.8" height="3.4" fill="none" stroke="#fff" stroke-width=".8"/><path d="M2.6 3.3L5 5.3l2.4-2" fill="none" stroke="#fff" stroke-width=".8"/></svg>info@trexolan.co</li>
    <li><svg class="icon" viewBox="0 0 10 10"><circle cx="5" cy="5" r="5" fill="#ed1c24"/><circle cx="5" cy="5" r="2.8" fill="none" stroke="#fff" stroke-width=".7"/><path d="M2.2 5h5.6M5 2.2v5.6" stroke="#fff" stroke-width=".6"/></svg>www.trexolan.co.uk</li>
  </ul>

  <div class="recipient">
    <div class="recipient-name">ADA FERROW</div>
    <div>0123-456-789</div>
    <div>info@youremailaddress.com</div>
    <div class="addr">1234 City Your Ln. Suite<br>123 Ridgeford, TX 0000</div>
  </div>
  <div class="letter-date">12 December, 2023</div>

  <p class="letter-body p1">Lorem ipsum dolor sit amet, consectetuer adipiscing elit, sed diam nonummy nibh euismod tincidunt ut laoreet dolore magna aliquam erat volutpat. Ut wisi enim ad minim veniam, quis nostrud exerci tation ullamcorper suscipit lobortis nisl ut aliquip ex ea commodo consequat. Duis autem vel eum iriure dolor in hendrerit in vulputate velit esse molestie consequat, vel illum dolore eu feugiat nulla facilisis at vero eros et accumsan et iusto odio dignissim qui blandit praesent luptatum zzril delenit augue duis dolore te feugait nulla facilisi.</p>
  <p class="letter-body p2">Lorem ipsum dolor sit amet, cons ectetuer adipiscing elit, sed diam nonummy nibh euismod tincidunt ut laoreet dolore magna aliquam erat volutpat. Ut wisi enim ad minim veniam, quis nostrud exerci tation ullamcorper suscipit lobortis nisl ut aliquip ex ea commodo consequat.<br>Lorem ipsum dolor sit amet, consectetuer adipiscing elit, sed diam nonummy nibh euismod tincidunt ut laoreet dolore magna aliquam erat</p>
  <p class="letter-body p3">Lorem ipsum dolor sit amet, cons ectetuer adipiscing elit, sed diam nonummy nibh euismod tincidunt ut laoreet dolore magna aliquam erat volutpat. Ut wisi enim ad minim veniam, quis nostrud exerci tation ullamcorper suscipit lobortis nisl ut aliquip ex ea commodo consequat. Lorem ipsum dolor sit zamet, consectetuer adipiscing elit, sed diam nonummy nibh euismod tincidunt.</p>

  <div class="signoff">Managing Director</div>
  <div class="signature" role="img" aria-label="Handwritten signature of the managing director"></div>

  <div class="decor" role="img" aria-label="Faint background decoration of the company mark"></div>
  <div class="address-band">
    <svg class="pin" viewBox="0 0 9 12"><path d="M4.5 0.5a4 4 0 0 1 4 4c0 3-4 7-4 7s-4-4-4-7a4 4 0 0 1 4-4z" fill="none" stroke="#fff" stroke-width="1"/><circle cx="4.5" cy="4.5" r="1.4" fill="#fff"/></svg>
    Merrow Lane East<br>Brindle Vale, Northford<br>NF7 2QK
  </div>
</section>

<section class="sheet signature-card">
  <div class="decor" role="img" aria-label="Faint background decoration of the company mark"></div>
  <div class="brand"><span class="brand-dot"></span>Daventa Hubs &amp; Axles Ltd</div>
  <div class="sender-name">Tom Ravel</div>
  <div class="sender-role">Mangaer</div>
  <div class="role-rule"></div>
  <div class="info-band">
    <ul class="contacts">
      <li><svg class="icon" viewBox="0 0 10 10"><circle cx="5" cy="5" r="5" fill="#fff"/><path d="M3.2 2.6l1 .9-.5.8a3.5 3.5 0 0 0 2 2l.8-.5.9 1-.7.8A5 5 0 0 1 2.4 3.3z" fill="#ed1c24"/></svg>161 480 2291</li>
      <li><svg class="icon" viewBox="0 0 10 10"><circle cx="5" cy="5" r="5" fill="#fff"/><rect x="2.6" y="3.3" width="4.8" height="3.4" fill="none" stroke="#ed1c24" stroke-width=".8"/></svg>info@trexolan.co</li>
      <li><svg class="icon" viewBox="0 0 10 10"><circle cx="5" cy="5" r="5" fill="#fff"/><circle cx="5" cy="5" r="2.8" fill="none" stroke="#ed1c24" stroke-width=".8"/></svg>www.trexolan.co.uk</li>
    </ul>
    <div class="postal">Merrow Lane East<br>Brindle Vale, Northford<br>NF7 2QK</div>
    <div class="follow">
      <div class="follow-title">Follow us</div>
      <div class="social">
        <span><i></i>Pelmora</span>
        <span><i></i>zandoro</span>
        <span><i></i>Vorlant</span>
      </div>
    </div>
  </div>
</section>

</body>
</html>
```